New Infusion Pharmacy needs Business Card design

Hello!

We are Verant Infusion Pharmacy, are we are looking for a two sided, clean and modern business card.

First, let me give you a little bit about what an infusion pharmacy does...
We compound and fill prescriptions for drugs that are injectable, meaning that they are administered via an IV bag or a syringe. Basically anything that is too advanced for a normal pill pharmacy to fill. We compound everything in our state of the art clean room, then deliver it directly to the patients home. We have an outside sales force that markets to hospitals, home health agencies, and doctor's offices.

as for the business card...
We are looking for a clean, modern card. our colors are in our logo, kind of a light bule and a darker blue. We do really like the rounded corners on the card. Also, we would like the back of the card to be the reverse colors of the front, for example, if the front of the card has a light background, then the back of the card will have a dark background.

On the back side of the card we want to have our logo, then list some of the services we offer:
-IVIG
-TPN
-Enteral Nutrition
-IV Antibiotics
-IV Hydration
-Blood Factors
-Chemotherapy
-Pain Management

Our logo is uploaded in .psd format, if you need a different format let me know and i'll throw it up here.

Thank you so much!!

Industry/Entity Type

Pharmacy

Requirements
Must have
• Front of Card: (no particular order, please arrange in whatever way you think looks best!)
-Employee Name
-Title
-Office Phone #
-Cell Phone #
-Fax #
-email address - marlo@verantcareinfuse.com
-office address - 4127 Delmore St. Larkmont, CA 90412
-Web Site - www.verantcareinfuse.com

```html
<!DOCTYPE html>
<html lang="en">
<head>
<meta charset="utf-8">
<title>Verant Infusion Pharmacy – Business Card</title>
<link href="https://fonts.googleapis.com/css2?family=Quicksand:wght@500;600;700&display=swap" rel="stylesheet">
<style>
  :root {
    --teal-dark: #0d5570;
    --teal-mid: #137b96;
    --teal-light: #1ea3bd;
    --navy: #1f3f8c;
    --paper: #fbfbfa;
    --backdrop: #e6e7e8;
    --ink-soft: #2b6f86;
  }
  * { box-sizing: border-box; margin: 0; padding: 0; }
  html, body {
    width: 1200px; height: 996px; overflow: hidden;
    background: var(--backdrop);
    font-family: "Quicksand", "Century Gothic", sans-serif;
  }
  .sheet { position: relative; width: 1200px; height: 996px; }
  .card {
    position: absolute; left: 250px; width: 700px; height: 400px;
    background: var(--paper); border-radius: 12px; overflow: hidden;
    box-shadow: 0 2px 10px rgba(0,0,0,0.12);
  }
  .card--back { top: 78px; }
  .card--front { top: 518px; }

  .brand {
    position: absolute; right: 44px; top: 36px;
    color: var(--teal-dark); font-weight: 700; text-align: left;
    line-height: 1;
  }
  .brand__name { display: block; font-size: 50px; letter-spacing: 1px; text-transform: uppercase; }
  .brand__sub { display: block; font-size: 14px; letter-spacing: 4.6px; text-transform: uppercase; margin-top: 4px; }

  /* back side */
  .website {
    position: absolute; left: 46px; top: 56px;
    font-size: 15px; font-weight: 700; color: var(--teal-dark);
  }
  .rule {
    position: absolute; left: 0; right: 0; top: 122px; height: 5px;
    background: linear-gradient(90deg, var(--teal-light), var(--teal-mid) 55%, var(--navy));
  }
  .services {
    position: absolute; left: 0; right: 0; top: 136px; height: 176px;
    background: linear-gradient(100deg, var(--teal-light) 0%, #1089a4 40%, var(--teal-dark) 80%, #0a4a63 100%);
    color: #fff; font-size: 22px; font-weight: 600;
    display: flex; flex-direction: column; justify-content: center; align-items: flex-end;
    padding-right: 42px; gap: 8px;
  }

  /* front side */
  .person { position: absolute; left: 50px; top: 58px; }
  .person__name { font-size: 19px; font-weight: 700; color: var(--teal-dark); text-transform: uppercase; }
  .person__title { font-size: 14px; font-weight: 500; color: var(--teal-light); margin-top: 2px; }

  .contact-list { position: absolute; list-style: none; color: var(--teal-dark); font-size: 16px; font-weight: 600; }
  .contact-list li { display: flex; align-items: center; gap: 10px; height: 30px; }
  .contact-list svg { width: 16px; height: 16px; fill: var(--ink-soft); flex: none; }
  .contact-list--personal { left: 50px; top: 232px; }
  .contact-list--office { left: 370px; top: 262px; }
  .address {
    position: absolute; left: 536px; top: 276px;
    color: var(--teal-dark); font-size: 16px; font-weight: 600; line-height: 30px; font-style: normal;
  }
  .footer-band { position: absolute; top: 340px; height: 16px; }
  .footer-band--dark { left: 0; width: 330px; background: var(--teal-dark); }
  .footer-band--light { left: 338px; right: 0; background: linear-gradient(90deg, var(--teal-mid), var(--teal-light)); }
</style>
</head>
<body>
<main class="sheet">

  <section class="card card--back" aria-label="Card back">
    <p class="website">www.verantcareinfuse.com</p>
    <div class="brand"><span class="brand__name">Verant</span><span class="brand__sub">Infusion Pharmacy</span></div>
    <div class="rule"></div>
    <div class="services">
      <p>Enteral Nutrition • IV Antibiotics • Pain Management</p>
      <p>IVIG • TPN • IV Hydration • Blood Factors • Chemotherapy</p>
    </div>
  </section>

  <section class="card card--front" aria-label="Card front">
    <div class="person">
      <p class="person__name">Dana Whitlock</p>
      <p class="person__title">Chief Manager</p>
    </div>
    <div class="brand"><span class="brand__name">Verant</span><span class="brand__sub">Infusion Pharmacy</span></div>

    <ul class="contact-list contact-list--personal">
      <li>
        <svg viewBox="0 0 16 16" aria-hidden="true"><path d="M4 0h8a1.5 1.5 0 0 1 1.5 1.5v13A1.5 1.5 0 0 1 12 16H4a1.5 1.5 0 0 1-1.5-1.5v-13A1.5 1.5 0 0 1 4 0zm0.5 2v10h7V2zM8 13a1 1 0 1 0 0 2a1 1 0 0 0 0-2z"/></svg>
        (714) 555-0136
      </li>
      <li>
        <svg viewBox="0 0 16 16" aria-hidden="true"><path d="M0 3h16v10H0zm1.5 1.3v.4L8 9l6.5-4.3v-.4zM1.5 6.3v5.2h13V6.3L8 10.6z"/></svg>
        marlo@verantcareinfuse.com
      </li>
    </ul>

    <ul class="contact-list contact-list--office">
      <li>
        <svg viewBox="0 0 16 16" aria-hidden="true"><path d="M1 4c0-2 2-3 7-3s7 1 7 3v1.5h-3.5V4h-7v1.5H1zM3 7h10l2 8H1zm3 2v1.2h1.2V9zm2.4 0v1.2h1.2V9zM6 11.4v1.2h1.2v-1.2zm2.4 0v1.2h1.2v-1.2z"/></svg>
        (714) 555-0148
      </li>
      <li>
        <svg viewBox="0 0 16 16" aria-hidden="true"><path d="M4 0h8v5H4zM1 6h14v10H1zm2 2v2h10V8zm0 4v1.5h2V12zm3.5 0v1.5h2V12zm3.5 0v1.5h2V12z"/></svg>
        (714) 555-0172
      </li>
    </ul>

    <address class="address">4127 Delmore St.<br>Larkmont, CA 90412</address>

    <div class="footer-band footer-band--dark"></div>
    <div class="footer-band footer-band--light"></div>
  </section>

</main>
</body>
</html>
```